Web Developer Needs a Business Card Design

I need a personal business card design that represents me as a web developer for potential employers. I would like the background to be a dark color on the front for contrast with my logo and name. The back will have all my information along with a smaller version of the logo. I want something with a modern look and feel, not too conservative. This will be used for potential employers and freelance work.

Industry/Entity Type

Business

Contact Information for Business Card

Front should have my logo and name. The back should have all my personal information which would include: name: Tom Brevardi, phone: 570-614-9083, email: tombrevardi@mailwisp.com, website url: www.tombrevardi.com, logo, web developer.

Font styles to use
Sans Serif

Requirements
Must have
• Must include my logo. The color palette base color will be the logo color.

```html
<!DOCTYPE html>
<html lang="en">
<head>
<meta charset="utf-8">
<title>Tom Brevardi – Business Card</title>
<link rel="stylesheet" href="https://fonts.googleapis.com/css2?family=Marcellus&family=Arimo:ital@0;1&display=swap">
<style>
  :root {
    --bg-light: #5ae6c8;
    --bg-mid: #3f9c88;
    --bg-deep: #24594d;
    --bg-dark: #050807;
    --ink: #5de3c4;
  }
  * { margin: 0; padding: 0; box-sizing: border-box; }
  html, body {
    width: 1200px;
    height: 690px;
    overflow: hidden;
    background: var(--bg-dark);
  }
  .card {
    position: relative;
    width: 1200px;
    height: 690px;
    overflow: hidden;
    background: linear-gradient(160deg,
      var(--bg-light) 0%,
      var(--bg-mid) 30%,
      var(--bg-deep) 62%,
      var(--bg-dark) 100%);
    color: var(--ink);
  }
  .identity {
    position: absolute;
    right: 39px;
    top: 295px;
    text-align: right;
  }
  .identity__name {
    font-family: "Marcellus", serif;
    font-weight: 400;
    font-size: 90px;
    line-height: 1;
    letter-spacing: 0.5px;
    padding: 0 15px 4px 8px;
    border-bottom: 4px solid var(--ink);
    display: inline-block;
  }
  .identity__role {
    font-family: "Arimo", Arial, sans-serif;
    font-style: italic;
    font-size: 38px;
    line-height: 44px;
    margin-top: 6px;
    padding-right: 15px;
  }
  .contact {
    position: absolute;
    left: 0;
    top: 520px;
    font-family: "Arimo", Arial, sans-serif;
    font-size: 37px;
    line-height: 43px;
    border-collapse: collapse;
  }
  .contact td { padding: 0; white-space: nowrap; }
  .contact__label { width: 194px; text-align: center; }
  .contact__sep { width: 78px; padding-left: 40px; }
</style>
</head>
<body>
  <main class="card">
    <header class="identity">
      <h1 class="identity__name">Tom Brevardi</h1>
      <p class="identity__role">logo and web developer</p>
    </header>
    <table class="contact">
      <tr><td class="contact__label">phone</td><td class="contact__sep">:</td><td class="contact__value">570-614-9083</td></tr>
      <tr><td class="contact__label">email</td><td class="contact__sep">:</td><td class="contact__value">tombrevardi@mailwisp.com</td></tr>
      <tr><td class="contact__label">website</td><td class="contact__sep">:</td><td class="contact__value">www.tombrevardi.com</td></tr>
    </table>
  </main>
</body>
</html>
```